Vorential Health Posters

Two posters needed to introduce our new package pricing, called our SPARK and GLOW programs. Our current posters are attached, these two new posters should be similar design and layout. The docx attached has what information should be on each poster. (vorentialhealth.com)

```html
<!DOCTYPE html>
<html lang="en">
<head>
<meta charset="utf-8">
<title>Vorential Health – Glow Package Poster</title>
<link href="https://fonts.googleapis.com/css2?family=Arvo:wght@400;700&family=Michroma&family=Exo+2:wght@700&display=swap" rel="stylesheet">
<style>
  :root {
    --page-bg: #c9c8c9;
    --photo-dark: #3e3d3f;
    --photo-mid: #6b6567;
    --photo-warm: #7a6259;
    --brand-red: #b3161c;
    --bar-black: #161616;
    --white: #ffffff;
    --footer-bg: #e3e3e3;
    --ink: #1a1a1a;
  }
  * { margin: 0; padding: 0; box-sizing: border-box; }
  html, body { width: 994px; height: 1200px; overflow: hidden; background: var(--page-bg); }
  .poster {
    position: absolute; left: 103px; top: 84px;
    width: 787px; height: 1019px;
    background: var(--footer-bg); overflow: hidden;
  }
  .hero-photo {
    position: absolute; left: 0; top: 0; width: 787px; height: 873px;
    background:
      radial-gradient(ellipse 380px 520px at 590px 300px, var(--photo-warm) 0%, transparent 70%),
      linear-gradient(100deg, var(--photo-dark) 0%, var(--photo-mid) 45%, var(--photo-dark) 100%);
  }
  .brand-name {
    position: absolute; left: 63px; top: 84px; width: 560px;
    font-family: "Michroma", sans-serif; font-size: 50px; line-height: 1;
    color: var(--brand-red); letter-spacing: 2px; text-align: center;
  }
  .package-title {
    position: absolute; left: 65px; top: 262px;
    font-family: "Arvo", serif; font-weight: 700; font-size: 62px; line-height: 1;
    color: var(--white); text-shadow: 2px 3px 4px rgba(0,0,0,.55);
  }
  .tagline {
    position: absolute; right: 51px; top: 375px; text-align: right;
    font-family: "Exo 2", sans-serif; font-weight: 700; font-size: 29px; line-height: 41px;
    color: var(--white); text-shadow: 2px 2px 3px rgba(0,0,0,.6);
  }
  .product-vial {
    position: absolute; left: 42px; top: 405px; width: 295px; height: 469px;
    border-radius: 26px 26px 18px 18px;
    background: linear-gradient(180deg, #f2f2f2 0%, #f2f2f2 11%, #b9b9bb 14%, #8a8a8d 30%, #5b5b5e 55%, #8d8d90 90%, #cfcfd1 100%);
  }
  .benefits { position: absolute; left: 0; top: 0; list-style: none; }
  .benefit {
    position: absolute; left: 314px; width: 391px; height: 50px;
    background: var(--bar-black); border-radius: 0 26px 26px 0;
    text-align: center; padding-right: 70px;
    font-family: "Michroma", sans-serif; line-height: 1;
  }
  .benefit:first-child { left: 306px; width: 399px; border-radius: 26px; }
  .benefit-verb { display: block; margin-top: 5px; font-size: 15px; color: var(--brand-red); font-weight: 700; }
  .benefit-goal { display: block; margin-top: 7px; font-size: 15px; color: var(--white); }
  .benefit-tick { position: absolute; right: 27px; top: 4px; width: 42px; height: 42px; }
  .powered-by {
    position: absolute; right: 51px; top: 884px;
    font-family: "Arvo", serif; font-size: 18px; color: var(--brand-red);
  }
  .offer-line {
    position: absolute; left: 34px; top: 934px;
    font-family: "Arvo", serif; font-size: 28.5px; color: var(--brand-red); white-space: nowrap;
  }
  .offer-terms {
    position: absolute; left: 35px; top: 970px;
    font-family: "Arvo", serif; font-weight: 700; font-size: 20.5px; color: var(--ink);
    white-space: nowrap; letter-spacing: -0.4px;
  }
</style>
</head>
<body>
<main class="poster">
  <div class="hero-photo" role="img" aria-label="Photo of a muscular shirtless man holding a dumbbell against a grey concrete wall"></div>

  <div class="brand-name">VORENTIAL</div>
  <h1 class="package-title">GLOW PACKAGE</h1>
  <p class="tagline">Burn Fat. Boost Energy<br>Transform Your Body</p>

  <div class="product-vial" role="img" aria-label="Glass vial with white cap and dark product label"></div>

  <ul class="benefits">
    <li class="benefit" style="top:477px"><span class="benefit-verb">INCREASE</span><span class="benefit-goal">FAT LOSS</span>
      <svg class="benefit-tick" viewBox="0 0 42 42"><rect x="2" y="8" width="32" height="32" fill="none" stroke="#fff" stroke-width="2.5"/><path d="M8 24 L16 33 L38 5" fill="none" stroke="#fff" stroke-width="6" stroke-linecap="round" stroke-linejoin="round"/></svg></li>
    <li class="benefit" style="top:562px"><span class="benefit-verb">BOOST</span><span class="benefit-goal">METABOLISM</span>
      <svg class="benefit-tick" viewBox="0 0 42 42"><rect x="2" y="8" width="32" height="32" fill="none" stroke="#fff" stroke-width="2.5"/><path d="M8 24 L16 33 L38 5" fill="none" stroke="#fff" stroke-width="6" stroke-linecap="round" stroke-linejoin="round"/></svg></li>
    <li class="benefit" style="top:647px"><span class="benefit-verb">IMPROVE</span><span class="benefit-goal">SLEEP</span>
      <svg class="benefit-tick" viewBox="0 0 42 42"><rect x="2" y="8" width="32" height="32" fill="none" stroke="#fff" stroke-width="2.5"/><path d="M8 24 L16 33 L38 5" fill="none" stroke="#fff" stroke-width="6" stroke-linecap="round" stroke-linejoin="round"/></svg></li>
    <li class="benefit" style="top:725px"><span class="benefit-verb">PROTECT</span><span class="benefit-goal">MUSCLE MASS</span>
      <svg class="benefit-tick" viewBox="0 0 42 42"><rect x="2" y="8" width="32" height="32" fill="none" stroke="#fff" stroke-width="2.5"/><path d="M8 24 L16 33 L38 5" fill="none" stroke="#fff" stroke-width="6" stroke-linecap="round" stroke-linejoin="round"/></svg></li>
    <li class="benefit" style="top:802px"><span class="benefit-verb">INCREASE</span><span class="benefit-goal">ENERGY</span>
      <svg class="benefit-tick" viewBox="0 0 42 42"><rect x="2" y="8" width="32" height="32" fill="none" stroke="#fff" stroke-width="2.5"/><path d="M8 24 L16 33 L38 5" fill="none" stroke="#fff" stroke-width="6" stroke-linecap="round" stroke-linejoin="round"/></svg></li>
  </ul>

  <p class="powered-by">Powered by Peptides + TRT</p>
  <p class="offer-line">One Low Monthly Price — Save BIG Over the Year</p>
  <p class="offer-terms">3 MONTHS FREE WHEN YOU STAY COMMITTED ALL YEAR</p>
</main>
</body>
</html>
```